innovative investment real estate sales firm

We are a uniquely collabrative firm that seeks to bring a conultative approach to uncovering hidden opportunities for our clients, our website needs to convey our client focused approach. Our firm specializes in the sale of apartment properties in Southern California. We have a team of researchers, transaction coordinators and marketing personal to support our geographically specialized advisers. We need a website that introduces clients to our unique way of better helping them achieve their investment goals.

Target Market(s)

High net worth individuals and families

Industry/Entity Type

Real Estate Agent

Font styles to use
Other font styles liked:
• please use font provided

Requirements
Must have
• Stories of our recent projects
• Features on our people
• email capture for viewing inventory
• content that showcases our unique consultative approach that uncovers unrealized opportunities

```html
<!DOCTYPE html>
<html lang="en">
<head>
<meta charset="utf-8">
<title>Meridian Crest Advisers — Multifamily Properties</title>
<link href="https://fonts.googleapis.com/css2?family=Lato:wght@400;700;900&display=swap" rel="stylesheet">
<style>
:root{
  --teal:#1a9db3;
  --teal-dark:#12849a;
  --green:#8dc63f;
  --ink:#2d3036;
  --charcoal:#3e4249;
  --grey-text:#555a60;
  --light:#eeeff0;
  --white:#ffffff;
}
*{box-sizing:border-box;margin:0;padding:0}
html,body{width:1200px;height:4380px;overflow:hidden}
body{font-family:'Lato',Arial,sans-serif;color:var(--ink);background:var(--white);position:relative}
.abs{position:absolute}
.section-title{font-size:38px;font-weight:700;text-transform:uppercase;letter-spacing:.5px;color:var(--ink)}
.section-title span{color:var(--teal)}
.rule{width:46px;height:4px;background:var(--green);margin-top:10px}
.center{text-align:center}
.center .rule{margin:10px auto 0}
.btn-dark{display:inline-block;background:var(--charcoal);color:#fff;font-size:14px;font-weight:700;padding:8px 18px;letter-spacing:.5px}
.btn-dark::after{content:" \00BB"}
p{font-size:15px;line-height:1.6;color:var(--grey-text)}

/* header */
.topbar{left:330px;top:0;width:870px;height:64px;background:var(--charcoal);clip-path:polygon(30px 0,100% 0,100% 100%,0 100%)}
.topbar .phone{position:absolute;left:60px;top:18px;color:#fff;font-size:24px;font-weight:700;display:flex;align-items:center;gap:12px}
.topbar .consult{position:absolute;right:80px;top:14px;background:#fff;color:var(--ink);font-size:15px;font-weight:700;padding:8px 22px;border-radius:20px;display:flex;align-items:center;gap:8px}
.brand{left:96px;top:22px;display:flex;align-items:center;gap:12px}
.brand .mark{width:50px;height:50px;background:var(--teal)}
.brand .name{font-size:22px;font-weight:900;color:var(--charcoal);letter-spacing:1px;line-height:1.1}
.nav{left:400px;top:64px;height:46px;display:flex;align-items:stretch}
.nav a{display:flex;align-items:center;padding:0 28px;font-size:14px;font-weight:700;color:#fff;text-decoration:none}
.navbar{left:380px;top:64px;width:820px;height:46px;background:var(--teal)}
.nav a.active{background:var(--green)}

/* hero */
.hero{left:0;top:110px;width:1200px;height:605px;background:linear-gradient(120deg,#c9d3d8,#8c9aa3 55%,#5d6870)}
.hero-label{left:100px;top:598px;width:470px;height:102px;background:var(--teal);color:#fff;font-size:30px;font-weight:700;text-transform:uppercase;padding:16px 24px;line-height:1.3}

/* about */
.about-photo{left:600px;top:790px;width:600px;height:440px;background:linear-gradient(135deg,#9fb3c2,#5e6f7c);clip-path:polygon(60px 0,100% 0,100% 100%,0 100%)}
.about{left:100px;top:770px;width:540px}
.about h4{font-size:17px;font-weight:700;margin:28px 0 8px}
.about ul{list-style:none}
.about li{font-size:15px;line-height:1.6;color:var(--grey-text);padding-left:18px;position:relative;margin-bottom:6px}
.about li::before{content:"";position:absolute;left:0;top:8px;width:7px;height:7px;border-radius:50%;background:var(--teal)}

/* services */
.services-bg{left:0;top:1255px;width:1200px;height:525px;background:linear-gradient(180deg,#a8abae,#6d7175)}
.services-panel{left:100px;top:1322px;width:1000px;height:390px;background:rgba(255,255,255,.92);padding-top:38px}
.services-row{display:flex;justify-content:space-around;margin-top:30px}
.service{width:280px;text-align:center}
.service .ico{width:88px;height:88px;border-radius:50%;background:var(--teal);margin:0 auto 12px;display:flex;align-items:center;justify-content:center}
.service h3{font-size:19px;font-weight:700;margin-bottom:6px}
.service p{font-size:14px;margin-bottom:14px}

/* why */
.why{left:100px;top:1850px;width:440px}
.why-item{display:flex;gap:22px;margin-top:30px}
.why-item .ico{flex:none;width:70px;height:70px;border-radius:50%;background:var(--charcoal);border:4px solid #dfe1e3;display:flex;align-items:center;justify-content:center}
.why-item h3{font-size:17px;font-weight:700;color:var(--teal);margin-bottom:4px}
.why-item p{font-size:13px;line-height:1.5}
.why-item p b{color:var(--teal);font-weight:400}
.testi{left:530px;top:1868px;width:670px;height:454px;background:var(--teal);clip-path:polygon(0 0,100% 0,100% 100%,60px 100%,0 100%)}
.testi-inner{position:absolute;left:170px;top:60px;width:460px}
.testi h2{font-size:38px;font-weight:700;color:#fff;text-transform:uppercase;margin-bottom:22px}
.quote{background:var(--teal-dark);border-left:4px solid #7fd0dd;padding:18px 24px;font-size:14px;font-style:italic;color:#e8f7fa;line-height:1.6}
.person{display:flex;align-items:center;gap:18px;margin-top:22px;color:#fff;font-size:17px;font-weight:700}
.avatar{width:78px;height:78px;border-radius:50%;background:#c6ccd0;border:4px solid #fff}
.dots{display:flex;gap:8px;margin-top:24px}
.dots i{width:9px;height:9px;border-radius:50%;border:1px solid #fff}
.dots i:first-child{background:#fff}

/* properties */
.props-bg{left:0;top:2380px;width:1200px;height:445px;background:var(--light)}
.props-title{left:0;top:2420px;width:1200px}
.prop{top:2510px;width:540px;height:235px;background:#fff;box-shadow:0 1px 4px rgba(0,0,0,.12)}
.prop .photo{position:absolute;left:0;top:0;width:190px;height:195px;background:linear-gradient(160deg,#a7b8c6,#6a5d52)}
.prop .body{position:absolute;left:200px;top:10px;right:10px}
.prop h3{font-size:16px;font-weight:700;margin-bottom:10px}
.prop .bar{display:flex;justify-content:space-between;align-items:center;background:var(--teal);color:#fff;padding:8px 12px}
.prop .bar b{font-size:22px}
.prop .bar span{font-size:14px;font-weight:700}
.prop p{font-size:13px;margin-top:10px}
.prop .more{font-size:13px;color:var(--teal);margin-top:6px}
.prop .foot{position:absolute;left:0;bottom:0;width:100%;height:40px;background:var(--charcoal);color:#fff;font-size:13px;display:flex;align-items:center;gap:40px;padding-left:16px}
.prop .foot .go{position:absolute;right:0;top:0;width:44px;height:40px;background:#5a5f66;display:flex;align-items:center;justify-content:center}
.arrow-side{color:#9aa0a5;font-size:34px}

/* team */
.team-bg{left:0;top:2825px;width:1200px;height:535px;background:linear-gradient(180deg,#55595e,#2e3135)}
.team-panel{left:100px;top:2892px;width:1000px;height:393px;background:#f4f5f6;padding-top:40px}
.team-row{display:flex;justify-content:center;gap:30px;margin-top:30px}
.member{width:300px;background:#fff;padding:18px;box-shadow:0 1px 4px rgba(0,0,0,.12)}
.member .top{display:flex;gap:18px}
.member .pic{width:106px;height:106px;border-radius:50%;background:#b9c1c7;border:4px solid #e6e8ea;flex:none}
.member h3{font-size:17px;font-weight:700;color:var(--teal);line-height:1.3;text-align:center}
.member .info{font-size:12px;color:var(--grey-text);text-align:center;line-height:1.8}
.member .btns{display:flex;gap:12px;margin-top:12px}
.member .btns span{flex:1;font-size:11px;font-weight:700;text-align:center;padding:7px 0;color:#fff}
.b-teal{background:var(--teal)}.b-dark{background:var(--charcoal)}

/* blog */
.blog-title{left:0;top:3420px;width:1200px}
.post{top:3505px;width:310px;height:335px;background:#fff;box-shadow:0 1px 5px rgba(0,0,0,.15)}
.post .photo{height:200px;background:linear-gradient(180deg,#b7cfe2,#7e8f9c)}
.post .date{position:absolute;right:0;top:150px;width:52px;height:52px;background:var(--teal);color:#fff;text-align:center;font-size:13px;line-height:1.1;padding-top:6px}
.post .date b{font-size:20px;display:block}
.post h3{font-size:17px;font-weight:700;margin:14px 12px 6px}
.post p{font-size:13px;margin:0 12px}
.post .corner{position:absolute;right:0;bottom:0;width:0;height:0;border-left:26px solid transparent;border-bottom:26px solid var(--teal)}

/* contact */
.map{left:500px;top:3905px;width:700px;height:415px;background:linear-gradient(135deg,#dfe6dc,#c9d8e6 60%,#a9c7df)}
.contact{left:0;top:3900px;width:640px;height:420px;background:var(--charcoal);clip-path:polygon(0 0,500px 0,640px 100%,0 100%)}
.contact-inner{position:absolute;left:100px;top:100px;color:#fff}
.contact h2{font-size:30px;font-weight:700;text-transform:uppercase}
.contact .rule{margin-bottom:30px}
.c-row{display:flex;gap:22px;align-items:flex-start;margin-bottom:26px;font-size:16px;color:#fff}
.c-row .ico{width:34px;height:34px;border-radius:50%;background:var(--teal);flex:none;display:flex;align-items:center;justify-content:center}
.c-row small{display:block;font-size:13px;color:#cfd2d6;line-height:1.5}
.newsletter{left:540px;top:3960px;width:660px;height:50px;background:var(--teal);display:flex;align-items:center;gap:20px;padding-left:14px}
.newsletter .label{color:#fff;font-size:24px;font-weight:700;display:flex;align-items:center;gap:10px}
.newsletter .field{width:290px;height:34px;background:#fff;font-size:13px;color:#888;padding:9px 10px}
.newsletter .go{width:40px;height:34px;background:var(--charcoal);color:#fff;font-weight:700;font-size:15px;display:flex;align-items:center;justify-content:center}
.pin-card{left:840px;top:4180px;width:230px;background:var(--teal);color:#fff;font-size:14px;padding:10px 14px;line-height:1.4}
.footer{left:0;top:4320px;width:1200px;height:60px;background:var(--teal);color:#fff;font-size:14px;font-weight:700;display:flex;align-items:center;justify-content:space-between;padding:0 100px}
.social{display:flex;gap:8px}
.social i{width:26px;height:26px;border-radius:50%;background:#fff;opacity:.9}
</style>
</head>
<body>

<!-- header -->
<div class="abs brand"><div class="mark"></div><div class="name">MERIDIAN CREST<br>ADVISERS</div></div>
<div class="abs topbar">
  <div class="phone">
    <svg width="22" height="22" viewBox="0 0 24 24"><path fill="#fff" d="M6.6 10.8a15 15 0 0 0 6.6 6.6l2.2-2.2c.3-.3.7-.4 1-.2 1.1.4 2.3.6 3.6.6.6 0 1 .4 1 1V20c0 .6-.4 1-1 1A17 17 0 0 1 3 4c0-.6.4-1 1-1h3.5c.6 0 1 .4 1 1 0 1.3.2 2.5.6 3.6.1.3 0 .7-.2 1z"/></svg>
    123-456-7890
  </div>
  <div class="consult"><svg width="16" height="16" viewBox="0 0 16 16"><circle cx="8" cy="8" r="7" fill="var(--green)"/></svg>Free Consultation</div>
</div>
<div class="abs navbar"></div>
<nav class="abs nav">
  <a class="active">HOME</a><a>ABOUT US</a><a>SERVICES</a><a>PROPERTIES</a><a>BLOG</a><a>CONTACT US</a>
</nav>

<!-- hero -->
<div class="abs hero" role="img" aria-label="Advisers meeting clients in a bright apartment with city view"></div>
<svg class="abs" style="left:0;top:640px" width="1200" height="80"><polygon points="0,80 580,80 620,0 0,0" fill="none"/><polygon points="560,80 620,0 680,80" fill="var(--ink)" opacity="0"/></svg>
<div class="abs hero-label">Meridian Crest Advisers<br>Multifamily Properties</div>

<!-- about -->
<svg class="abs" style="left:540px;top:700px" width="660" height="100"><polygon points="0,100 660,100 660,0 60,0" fill="#fff"/><polygon points="20,40 60,0 90,90" fill="var(--ink)"/></svg>
<div class="abs about-photo" role="img" aria-label="Team of advisers gathered around a laptop"></div>
<div class="abs about">
  <h2 class="section-title">About <span>Us</span></h2><div class="rule"></div>
  <h4>About The Team</h4>
  <p>Lorem ipsum dolor sit amet, consectetuer adipiscing elit, sed diam nonum nibh euismod tincidunt ut laoreet dolore magna aliquam erat volutpat. Ut wisi enim ad minim veniam, quis nostrud exerci tation ullamcorper suscipit lobortis nisl ut aliquip ex ea commo.</p>
  <h4>What Sets Us Apartment</h4>
  <ul>
    <li>Sed ut perspiciatis unde omnis iste natus error sit voluptatem cusantium.</li>
    <li>At vero eos et accusamus et iusto odio dignissimos ducimus qui blanditiis praesentium voluptatum deleniti atque corrupti quos dolores et quas.</li>
  </ul>
  <div class="btn-dark" style="margin-top:12px">MORE</div>
</div>

<!-- services -->
<div class="abs services-bg" role="img" aria-label="Black and white city skyline"></div>
<div class="abs services-panel center">
  <h2 class="section-title">Our <span>Services</span></h2><div class="rule"></div>
  <div class="services-row">
    <div class="service"><div class="ico"><svg width="40" height="40" viewBox="0 0 24 24"><path fill="#fff" d="M2 12l20-9-7 19-3-8z"/></svg></div><h3>Advantages</h3><p>Lorem ipsum dolor sit amet, consectetur adipiscing elit, sed do eiusmod tempor incididunt ut labore.</p><div class="btn-dark">MORE</div></div>
    <div class="service"><div class="ico"><svg width="44" height="44" viewBox="0 0 24 24" fill="none" stroke="#fff" stroke-width="1.6"><circle cx="12" cy="12" r="3"/><circle cx="4" cy="5" r="2"/><circle cx="20" cy="5" r="2"/><circle cx="4" cy="19" r="2"/><circle cx="20" cy="19" r="2"/><path d="M6 6l4 4M18 6l-4 4M6 18l4-4M18 18l-4-4"/></svg></div><h3>Associations</h3><p>Lorem ipsum dolor sit amet, consectetur adipiscing elit, sed do eiusmod tempor incididunt ut labore.</p><div class="btn-dark">MORE</div></div>
    <div class="service"><div class="ico"><svg width="44" height="44" viewBox="0 0 24 24" fill="none" stroke="#fff" stroke-width="1.6"><circle cx="12" cy="6" r="3"/><path d="M6 21v-5a6 6 0 0 1 12 0v5"/></svg></div><h3>Incentives</h3><p>Lorem ipsum dolor sit amet, consectetur adipiscing elit, sed do eiusmod tempor incididunt ut labore.</p><div class="btn-dark">MORE</div></div>
  </div>
</div>

<!-- why choose / testimonials -->
<svg class="abs" style="left:500px;top:1780px" width="200" height="610"><polygon points="0,0 90,88 90,0" fill="var(--ink)"/><polygon points="30,545 90,545 50,610" fill="var(--ink)"/></svg>
<div class="abs why">
  <h2 class="section-title">Why <span>Choose Us</span></h2><div class="rule"></div>
  <div class="why-item"><div class="ico"><svg width="30" height="30" viewBox="0 0 24 24"><path fill="#fff" d="M12 2a7 7 0 0 0-4 12.7V18h8v-3.3A7 7 0 0 0 12 2zM9 20h6v2H9z"/></svg></div><div><h3>Knowledge</h3><p>Lorem ipsum dolor sit amet, consectetur adipis elit, sed do eiusmod te ullamco laboris... <b>[ + ]</b></p></div></div>
  <div class="why-item"><div class="ico"><svg width="32" height="32" viewBox="0 0 24 24" fill="none" stroke="#fff" stroke-width="2"><path d="M2 12l5-5 5 3 5-3 5 5-7 7z"/></svg></div><div><h3>Commitment</h3><p>Lorem ipsum dolor sit amet, consectetur adipis elit, sed do eiusmod te ullamco laboris... <b>[ + ]</b></p></div></div>
  <div class="why-item"><div class="ico"><svg width="32" height="32" viewBox="0 0 24 24" fill="none" stroke="#fff" stroke-width="2"><circle cx="12" cy="12" r="9"/><circle cx="12" cy="12" r="5"/><circle cx="12" cy="12" r="1.5" fill="#fff"/></svg></div><div><h3>Approach</h3><p>Lorem ipsum dolor sit amet, consectetur adipis elit, sed do eiusmod te ullamco laboris... <b>[ + ]</b></p></div></div>
  <div class="why-item"><div class="ico"><svg width="30" height="30" viewBox="0 0 24 24"><path fill="#fff" d="M2 10h4v11H2zM8 21h10l3-8v-3h-7l1-5-2-2-5 6z"/></svg></div><div><h3>Reputation</h3><p>Lorem ipsum dolor sit amet, consectetur adipis elit, sed do eiusmod te ullamco laboris... <b>[ + ]</b></p></div></div>
</div>
<div class="abs testi">
  <div class="testi-inner">
    <h2>Clients Testimonials</h2>
    <div class="quote">“ Lorem ipsum dolor sit amet consetuge sed diau nibhil ut dolore mag an er wisi enim ad minim veni quis nostrud exerci tationurse lorem ipsum dol sit ametnim sed diammmy nibh eud tincidunt ut laoreet dolore aliqur minim eni quis nostrud.</div>
    <div class="person"><div class="avatar" role="img" aria-label="Client portrait"></div>Daniel Marsh</div>
    <div class="dots"><i></i><i></i><i></i><i></i></div>
  </div>
</div>

<!-- properties -->
<div class="abs props-bg"></div>
<div class="abs props-title center"><h2 class="section-title">Our <span>Properties</span></h2><div class="rule"></div></div>
<div class="abs arrow-side" style="left:60px;top:2590px">&#8249;</div>
<div class="abs arrow-side" style="left:1120px;top:2590px">&#8250;</div>
<div class="abs prop" style="left:100px">
  <div class="photo" role="img" aria-label="Modern apartment tower"></div>
  <div class="body"><h3>Lorem Ipsum Dolor Sit Amet</h3><div class="bar"><b>$1.2m</b><span>Apartment</span></div><p>Lorem ipsum dolor sit amet, consectetur adipiscing elit, sed do eiusmod tempor</p><div class="more">More Details »</div></div>
  <div class="foot"><span>&#9679; Harborview, West Coastal</span><span>&#9635; Approx 6,000 Square feet</span><div class="go">&#10140;</div></div>
</div>
<div class="abs prop" style="left:640px">
  <div class="photo" role="img" aria-label="Apartment complex at sunset"></div>
  <div class="body"><h3>Lorem Ipsum Dolor Sit Amet</h3><div class="bar"><b>$1.8m</b><span>Apartment</span></div><p>Lorem ipsum dolor sit amet, consectetur adipiscing elit, sed do eiusmod tempor</p><div class="more">More Details »</div></div>
  <div class="foot"><span>&#9679; Harborview, West Coastal</span><span>&#9635; Approx 6,000 Square feet</span><div class="go">&#10140;</div></div>
</div>

<!-- team -->
<div class="abs team-bg" role="img" aria-label="Dark city skyline"></div>
<div class="abs arrow-side" style="left:62px;top:3090px;color:#fff">&#8249;</div>
<div class="abs arrow-side" style="left:1118px;top:3090px;color:#fff">&#8250;</div>
<div class="abs team-panel center">
  <h2 class="section-title">Our <span>Team</span></h2><div class="rule"></div>
  <div class="team-row">
    <div class="member"><div class="top"><div class="pic" role="img" aria-label="Adviser portrait"></div><div><h3>Lorem Ipsum<br>Dolor</h3><div class="info">President<br>123-456-7890<br>info@meridiancrestadvisers.com</div></div></div><div class="btns"><span class="b-teal">ONLINE RESUME</span><span class="b-dark">VIEW MORE INFO</span></div></div>
    <div class="member"><div class="top"><div class="pic" role="img" aria-label="Adviser portrait"></div><div><h3>Lorem Ipsum<br>Dolor</h3><div class="info">President<br>123-456-7890<br>info@meridiancrestadvisers.com</div></div></div><div class="btns"><span class="b-teal">ONLINE RESUME</span><span class="b-dark">VIEW MORE INFO</span></div></div>
    <div class="member"><div class="top"><div class="pic" role="img" aria-label="Adviser portrait"></div><div><h3>Lorem Ipsum<br>Dolor</h3><div class="info">President<br>123-456-7890<br>info@meridiancrestadvisers.com</div></div></div><div class="btns"><span class="b-teal">ONLINE RESUME</span><span class="b-dark">VIEW MORE INFO</span></div></div>
  </div>
</div>

<!-- blog -->
<div class="abs blog-title center"><h2 class="section-title">Latest <span>Blog</span></h2><div class="rule"></div></div>
<div class="abs post" style="left:100px"><div class="photo" role="img" aria-label="White residential tower"></div><div class="date"><b>12</b>July</div><h3>Lorem ipsum dolor sit amet.</h3><p>Lorem ipsum dolor sit amet, consectetuer adi, sed diam nonummy nibh euismod tincidunt ut laoreet dolore magna.</p><div class="corner"></div></div>
<div class="abs post" style="left:445px"><div class="photo" role="img" aria-label="Apartment building with balconies"></div><div class="date"><b>12</b>July</div><h3>Lorem ipsum dolor sit amet.</h3><p>Lorem ipsum dolor sit amet, consectetuer adi, sed diam nonummy nibh euismod tincidunt ut laoreet dolore magna.</p><div class="corner"></div></div>
<div class="abs post" style="left:790px"><div class="photo" role="img" aria-label="Curved apartment block under blue sky"></div><div class="date"><b>12</b>July</div><h3>Lorem ipsum dolor sit amet.</h3><p>Lorem ipsum dolor sit amet, consectetuer adi, sed diam nonummy nibh euismod tincidunt ut laoreet dolore magna.</p><div class="corner"></div></div>

<!-- contact -->
<div class="abs map" role="img" aria-label="Street map of the office location"></div>
<div class="abs contact">
  <div class="contact-inner">
    <h2>Contact Us</h2><div class="rule"></div>
    <div class="c-row"><div class="ico"><svg width="16" height="16" viewBox="0 0 24 24"><path fill="#fff" d="M12 2a7 7 0 0 0-7 7c0 5 7 13 7 13s7-8 7-13a7 7 0 0 0-7-7zm0 9.5A2.5 2.5 0 1 1 12 6a2.5 2.5 0 0 1 0 5.5z"/></svg></div><div>Meridian Crest Advisers<small>Lorem Ipsum is simply dummy<br>text of the printing typesett.</small></div></div>
    <div class="c-row"><div class="ico"><svg width="16" height="16" viewBox="0 0 24 24"><path fill="#fff" d="M6.6 10.8a15 15 0 0 0 6.6 6.6l2.2-2.2c.3-.3.7-.4 1-.2 1.1.4 2.3.6 3.6.6.6 0 1 .4 1 1V20c0 .6-.4 1-1 1A17 17 0 0 1 3 4c0-.6.4-1 1-1h3.5c.6 0 1 .4 1 1 0 1.3.2 2.5.6 3.6.1.3 0 .7-.2 1z"/></svg></div><div style="padding-top:6px">123-456-7890</div></div>
    <div class="c-row"><div class="ico"><svg width="16" height="16" viewBox="0 0 24 24"><path fill="#fff" d="M2 5h20v14H2zm2 2v.5l8 5 8-5V7z"/></svg></div><div style="padding-top:6px">info@meridiancrestadvisers.com</div></div>
  </div>
</div>
<div class="abs newsletter">
  <div class="label"><svg width="30" height="30" viewBox="0 0 24 24"><circle cx="12" cy="12" r="11" fill="var(--green)"/><path fill="#fff" d="M6 8h12v8H6zm1 1v.4l5 3 5-3V9z"/></svg>Newsletter</div>
  <div class="field">Your e-mail</div><div class="go">Go</div>
</div>
<svg class="abs" style="left:820px;top:4140px" width="30" height="40" viewBox="0 0 24 32"><path fill="var(--teal)" d="M12 0a11 11 0 0 0-11 11c0 8 11 21 11 21s11-13 11-21A11 11 0 0 0 12 0z"/><circle cx="12" cy="11" r="4" fill="#fff"/></svg>
<div class="abs pin-card">Lorem Ipsum is simply dummy text of the printing typesett.</div>

<!-- footer -->
<div class="abs footer"><span>Copyright © 2017 Meridian Crest Advisers. All Rights Reserved.</span><div class="social"><i></i><i></i><i></i><i></i></div></div>

</body>
</html>
```